Tarvel Ridge LLC

Need Professional Business cards for New Investment Fund

Target Market(s)

High Quality investors

Industry/Entity Type

Financial

Contact Information for Business Card

Phone Number +1 555 284 6193
Name Pavel Orlinsky
Title Fund Manager
email po@FundTarvel.example
Website www.FundTarvel.example

Colors

Designer to choose colors to be used in the design.

Requirements
Must have
• Must have our Logo and all of the above. Must be made so lettering and loge can be raised

```html
<!DOCTYPE html>
<html lang="en">
<head>
<meta charset="utf-8">
<title>Tarvel Ridge LLC — Business Cards</title>
<link rel="stylesheet" href="https://fonts.googleapis.com/css2?family=Didact+Gothic&family=Arimo:wght@400&display=swap">
<style>
  :root {
    --stage: #2b2b2b;
    --card-dark: #434f40;
    --card-light: #ffffff;
    --brand-green: #1ee01a;
    --ink-dark: #434f40;
    --ink-text: #3a3a3a;
    --divider: #8a8a8a;
    --faint: rgba(255,255,255,0.07);
  }
  * { margin: 0; padding: 0; box-sizing: border-box; }
  html, body {
    width: 1200px; height: 880px; overflow: hidden;
    background: var(--stage);
  }
  .canvas { position: relative; width: 1200px; height: 880px; }

  .card {
    position: absolute;
    width: 620px; height: 354px;
    border-radius: 26px;
    overflow: hidden;
    box-shadow: 0 10px 30px rgba(0,0,0,0.45);
  }

  /* Front (dark) */
  .card--front { left: 70px; top: 70px; background: var(--card-dark); }
  .card--front .backdrop-mark {
    position: absolute; left: 40px; top: 90px;
    width: 230px; height: 230px;
    background: var(--faint);
  }
  .card--front .brand {
    position: absolute; left: 330px; top: 120px;
    display: flex; align-items: center; gap: 14px;
  }
  .brand-square {
    width: 34px; height: 34px; background: var(--brand-green);
  }
  .brand-name {
    font-family: "Didact Gothic", sans-serif;
    font-size: 34px; letter-spacing: 1px;
    text-transform: uppercase;
  }
  .card--front .brand-name { color: #ffffff; }

  /* Back (white) */
  .card--back { left: 510px; top: 456px; background: var(--card-light); }
  .card--back .brand {
    position: absolute; left: 38px; top: 150px;
    display: flex; align-items: center; gap: 12px;
  }
  .card--back .brand-square { width: 28px; height: 28px; }
  .card--back .brand-name { color: var(--ink-dark); font-size: 26px; }

  .divider {
    position: absolute; left: 290px; top: 80px;
    width: 1px; height: 190px; background: var(--divider);
  }

  .person { position: absolute; left: 322px; top: 86px; }
  .person-name {
    font-family: "Didact Gothic", sans-serif;
    font-size: 24px; color: var(--ink-text);
    text-transform: uppercase; letter-spacing: 0.5px;
  }
  .person-title {
    font-family: "Arimo", sans-serif;
    font-size: 15px; color: var(--ink-text); margin-top: 2px;
  }

  .contacts { position: absolute; left: 322px; top: 182px; list-style: none; }
  .contact {
    display: flex; align-items: center; gap: 10px;
    font-family: "Arimo", sans-serif; font-size: 15px;
    color: var(--ink-text); margin-bottom: 8px;
  }
  .contact-icon { width: 18px; height: 18px; flex: none; }
</style>
</head>
<body>
<main class="canvas">

  <section class="card card--front" aria-label="Card front">
    <div class="backdrop-mark" aria-hidden="true"></div>
    <div class="brand">
      <span class="brand-square" aria-hidden="true"></span>
      <span class="brand-name">Tarvel Ridge</span>
    </div>
  </section>

  <section class="card card--back" aria-label="Card back">
    <div class="brand">
      <span class="brand-square" aria-hidden="true"></span>
      <span class="brand-name">Tarvel Ridge</span>
    </div>

    <div class="divider" aria-hidden="true"></div>

    <div class="person">
      <h1 class="person-name">Pavel Orlinsky</h1>
      <p class="person-title">Fund Manager</p>
    </div>

    <ul class="contacts">
      <li class="contact">
        <svg class="contact-icon" viewBox="0 0 18 18" aria-hidden="true">
          <rect width="18" height="18" rx="4" fill="#434f40"/>
          <path d="M5 4.5 L7.2 4.5 L8 7 L6.8 8 Q8 10.4 10 11.2 L11 10 L13.5 10.8 L13.5 13 Q9 13.8 6.5 11 Q4.2 8.5 5 4.5 Z" fill="#1ee01a"/>
        </svg>
        <span>+1 555 284 6193</span>
      </li>
      <li class="contact">
        <svg class="contact-icon" viewBox="0 0 18 18" aria-hidden="true">
          <rect width="18" height="18" rx="4" fill="#434f40"/>
          <rect x="3.5" y="5" width="11" height="8" fill="#1ee01a"/>
          <path d="M3.5 5 L9 9.5 L14.5 5" fill="none" stroke="#434f40" stroke-width="1.2"/>
        </svg>
        <span>po@FundTarvel.example</span>
      </li>
      <li class="contact">
        <svg class="contact-icon" viewBox="0 0 18 18" aria-hidden="true">
          <rect width="18" height="18" rx="4" fill="#434f40"/>
          <circle cx="9" cy="9" r="5.2" fill="#1ee01a"/>
          <path d="M3.8 9 H14.2 M9 3.8 Q6.2 9 9 14.2 M9 3.8 Q11.8 9 9 14.2" fill="none" stroke="#434f40" stroke-width="0.9"/>
        </svg>
        <span>www.FundTarvel.example</span>
      </li>
    </ul>
  </section>

</main>
</body>
</html>
```